We need a flyer design to promote Pembury & Vance Landscaping and Lawn Maintenance.

The flyer needs to be have:-
1) A great head line ( When quality matters)
2) A really awesome offer ( no obligation free trial mow)
3) A sense of scarcity (Due to time restraints, we can only take limited number of free lawn jobs. This offer is only available to the first 20 callers)
4) A call to action (Call now to avoid disappointment)
5) Contact details (Pembury & Vance Landscaping and Lawn Maintenance 0472 586 307)

The layout of the entire flyer should come across to potential customers as

1) simple to understand what Pembury & Vance offer (not overcrowd with messages; the main aim is to communicate across our services.)

The list of services that Pembury & Vance provide will be:-

- Lawn Mowing - Pruning - Weeding
- Mulching - Edging - Hedging
- Trimming - Fertilising - Garden maintenance
- Weekly, fortnightly or monthly programs

Thank you.

```html
<!DOCTYPE html>
<html lang="en">
<head>
<meta charset="utf-8">
<title>Pembury &amp; Vance Landscaping – Flyer</title>
<link rel="stylesheet" href="https://fonts.googleapis.com/css2?family=Questrial&family=Mulish:ital,wght@1,400;1,800&family=Oswald:wght@400;500&family=Jost:wght@700&family=Archivo+Black&display=swap">
<style>
  :root {
    --page: #eef0ee;
    --sky-top: #4f9fdc;
    --sky-light: #cfe6f6;
    --band-light: rgba(236, 244, 250, 0.82);
    --title-brown: #3a2a1c;
    --grass-bright: #9fd84a;
    --grass-deep: #3f7d1c;
    --soil: #2c2114;
    --headline-bar: #2d4a25;
    --panel-green: #c6e2c2;
    --brand-green: #45a844;
    --ink: #111111;
    --white: #ffffff;
    --mower-grey: rgba(150, 150, 150, 0.38);
  }
  * { margin: 0; padding: 0; box-sizing: border-box; }
  html, body {
    width: 927px; height: 1200px; overflow: hidden;
    background: var(--page);
  }
  .flyer {
    position: absolute; left: 55px; top: 20px;
    width: 685px; height: 973px;
    transform: scale(1.1927); transform-origin: top left;
    background: var(--white);
    overflow: hidden;
  }
  .sky {
    position: absolute; left: 0; top: 0; width: 100%; height: 160px;
    background: linear-gradient(180deg, var(--sky-top) 0%, var(--sky-light) 100%);
  }
  .masthead {
    position: absolute; left: 0; top: 25px; width: 100%; height: 107px;
    background: var(--band-light);
    display: flex; align-items: center; justify-content: center;
    text-align: center;
  }
  .brand-name {
    font-family: "Questrial", sans-serif; font-weight: 400;
    font-size: 30px; line-height: 38px; color: var(--title-brown);
  }
  .lawn-photo {
    position: absolute; left: 0; top: 132px; width: 100%; height: 243px;
    background: linear-gradient(180deg, var(--sky-light) 0%, var(--grass-bright) 14%, var(--grass-deep) 55%, #4a3a22 66%, var(--soil) 100%);
  }
  .headline-bar {
    position: absolute; left: 0; top: 375px; width: 100%; height: 47px;
    background: var(--headline-bar);
    font-family: "Oswald", sans-serif; font-weight: 400;
    font-size: 31px; color: var(--white);
    text-align: center; line-height: 47px;
  }
  .offer {
    position: absolute; left: 0; top: 422px; width: 100%; height: 166px;
    background: var(--panel-green);
    font-family: "Mulish", sans-serif; font-style: italic; font-weight: 400;
    font-size: 22.5px; line-height: 33.5px; color: var(--ink);
    text-align: center; padding-top: 20px;
  }
  .offer strong { color: var(--brand-green); font-weight: 800; font-style: normal; }
  .mower-art {
    position: absolute; left: 192px; top: 430px; width: 490px; height: 543px;
    background: radial-gradient(ellipse at 55% 65%, var(--mower-grey) 0%, rgba(150,150,150,0.18) 55%, rgba(150,150,150,0) 75%);
  }
  .services {
    position: absolute; left: 0; top: 588px; width: 100%; height: 279px;
  }
  .services-title {
    position: relative;
    font-family: "Jost", sans-serif; font-weight: 700;
    font-size: 25px; color: var(--brand-green);
    text-align: center; margin-top: 16px;
  }
  .service-list {
    position: absolute; list-style: none; top: 70px;
    font-family: "Questrial", sans-serif; font-size: 21.5px; color: var(--ink);
  }
  .service-list.col-a { left: 110px; }
  .service-list.col-b { left: 327px; }
  .service-list li {
    position: relative; padding-left: 34px; line-height: 24px; margin-bottom: 9px;
  }
  .service-list li svg { position: absolute; left: 0; top: 3px; }
  .cta {
    position: absolute; left: 0; top: 867px; width: 100%; height: 106px;
    background: var(--panel-green);
  }
  .cta-icon { position: absolute; left: 58px; top: 20px; }
  .cta-line {
    position: absolute; left: 142px; top: 18px;
    font-family: "Oswald", sans-serif; font-weight: 500;
    font-size: 25px; color: var(--brand-green);
    transform: skewX(-10deg);
  }
  .cta-phone {
    position: absolute; left: 0; top: 58px; width: 100%;
    font-family: "Archivo Black", sans-serif;
    font-size: 25px; color: var(--ink); letter-spacing: 1px;
    text-align: center;
  }
</style>
</head>
<body>
<main class="flyer">
  <div class="sky" role="img" aria-label="Clear blue sky"></div>
  <header class="masthead">
    <h1 class="brand-name">Pembury &amp; Vance Landscaping<br>and Lawn Maintenance</h1>
  </header>
  <div class="lawn-photo" role="img" aria-label="Close-up photo of tall green lawn grass with roots and soil below"></div>
  <h2 class="headline-bar">When quality matters...</h2>
  <section class="offer">
    No obligation free trail mow!<br>
    Due to time restraints, we can only take a limited<br>
    number of free lawn jobs. This offer is only<br>
    available to the first <strong>20</strong> callers!
  </section>
  <div class="mower-art" role="img" aria-label="Faint grey silhouette of a push lawn mower"></div>
  <section class="services">
    <h3 class="services-title">Services</h3>
    <ul class="service-list col-a">
      <li><svg width="20" height="20" viewBox="0 0 20 20"><circle cx="10" cy="10" r="8.5" fill="none" stroke="#45a844" stroke-width="2"/><path d="M8.5 6.5 L12 10 L8.5 13.5" fill="none" stroke="#45a844" stroke-width="2"/></svg>Lawn Mowing</li>
      <li><svg width="20" height="20" viewBox="0 0 20 20"><circle cx="10" cy="10" r="8.5" fill="none" stroke="#45a844" stroke-width="2"/><path d="M8.5 6.5 L12 10 L8.5 13.5" fill="none" stroke="#45a844" stroke-width="2"/></svg>Pruning</li>
      <li><svg width="20" height="20" viewBox="0 0 20 20"><circle cx="10" cy="10" r="8.5" fill="none" stroke="#45a844" stroke-width="2"/><path d="M8.5 6.5 L12 10 L8.5 13.5" fill="none" stroke="#45a844" stroke-width="2"/></svg>Weeding</li>
      <li><svg width="20" height="20" viewBox="0 0 20 20"><circle cx="10" cy="10" r="8.5" fill="none" stroke="#45a844" stroke-width="2"/><path d="M8.5 6.5 L12 10 L8.5 13.5" fill="none" stroke="#45a844" stroke-width="2"/></svg>Mulching</li>
      <li><svg width="20" height="20" viewBox="0 0 20 20"><circle cx="10" cy="10" r="8.5" fill="none" stroke="#45a844" stroke-width="2"/><path d="M8.5 6.5 L12 10 L8.5 13.5" fill="none" stroke="#45a844" stroke-width="2"/></svg>Edging</li>
    </ul>
    <ul class="service-list col-b">
      <li><svg width="20" height="20" viewBox="0 0 20 20"><circle cx="10" cy="10" r="8.5" fill="none" stroke="#45a844" stroke-width="2"/><path d="M8.5 6.5 L12 10 L8.5 13.5" fill="none" stroke="#45a844" stroke-width="2"/></svg>Hedging</li>
      <li><svg width="20" height="20" viewBox="0 0 20 20"><circle cx="10" cy="10" r="8.5" fill="none" stroke="#45a844" stroke-width="2"/><path d="M8.5 6.5 L12 10 L8.5 13.5" fill="none" stroke="#45a844" stroke-width="2"/></svg>Trimming</li>
      <li><svg width="20" height="20" viewBox="0 0 20 20"><circle cx="10" cy="10" r="8.5" fill="none" stroke="#45a844" stroke-width="2"/><path d="M8.5 6.5 L12 10 L8.5 13.5" fill="none" stroke="#45a844" stroke-width="2"/></svg>Fertilizing</li>
      <li><svg width="20" height="20" viewBox="0 0 20 20"><circle cx="10" cy="10" r="8.5" fill="none" stroke="#45a844" stroke-width="2"/><path d="M8.5 6.5 L12 10 L8.5 13.5" fill="none" stroke="#45a844" stroke-width="2"/></svg>Garden maintenance</li>
      <li><svg width="20" height="20" viewBox="0 0 20 20"><circle cx="10" cy="10" r="8.5" fill="none" stroke="#45a844" stroke-width="2"/><path d="M8.5 6.5 L12 10 L8.5 13.5" fill="none" stroke="#45a844" stroke-width="2"/></svg>Weekly, fortnightly or<br>monthly programs</li>
    </ul>
  </section>
  <footer class="cta">
    <svg class="cta-icon" width="60" height="66" viewBox="0 0 60 66" aria-hidden="true">
      <path d="M12 6 C4 10 2 20 6 32 C10 44 20 56 34 60 C42 62 48 60 52 56 L44 44 C40 46 36 48 32 46 C26 42 22 34 20 26 C20 22 22 20 26 18 L20 4 C18 3 15 4 12 6 Z" fill="#45a844"/>
      <rect x="36" y="4" width="18" height="10" rx="3" fill="#45a844" transform="rotate(35 45 9)"/>
    </svg>
    <p class="cta-line">CALL NOW TO AVOID DISAPPOINTMENT</p>
    <p class="cta-phone">0472 586 307</p>
  </footer>
</main>
</body>
</html>
```